Etiketten-Design für Imkerei
Zielgruppe
Wir sind eine kleine Imkerei die sich vorwiegend auf Honig konzentriert. Waldhonig und Wald-Blütenhonig .
Zielgruppe sind alle die gerne Qualitätshonig aus der Region kaufen .
Aufgabenstellung
es sind 2 verschiedene Etiketten Größen für verschieden Nettofüllmengen :
250 g - H 3,5 cm ,B 12 cm
500 g - H 5 cm , B 17 cm
Honigsortenbezeichnung je einmal 'Wald' einmal 'Wald-Blüten' sollte aber möglich sein auch andere Honigsorten anzugeben.
die gesetzlichen Vorschriften der Schriftgröße für Adresse, Haltbarkeit und 100% Honig aus Österreich sind 1,2 mm immer vom kleinsten Buchstaben ausgehend . Ausgenommen NETTOFÜLLMENGE muss mind. 4 mm sein auch vom kleinsten Buchstaben ausgehend .
die Adresse und Mindestens Haltbar bis auf der linken Seite der Etikette( muss auf der gleichen Seite stehen) , in der Mitte Schriftzug mit Grafik wobei hier die Größe keiner Vorschrift unterliegt.
Sortenbezeichnung kann in der Mitte sein muss aber nicht und rechts neben Schriftzug „KOLMER`S HONIG“ die Nettofüllmenge , ganz rechts dann 100% Honig aus Österreich
Die Hintergrundfarbe der Etiketten sollten in Granitgrau- Schwarz lebendig also ähnlich wie marmoriert sein.
Schriftzug in der Mitte : ' Kolmer`s Honig ' das 'B' sollte eine Biene sein , den Rest überlasse ich Euch Profis . Schriftfarbe nicht Metallic oder Gold da die Deckel Silber sind. Fotos füge ich unten ein wobei es weder diese Biene sein muss noch der Schriftzug das ist nur ein Beispiel. Das ganze sollte edel und doch verspielt aussehen . Den Schriftzug Kolmer`s Honig möchte ich in weiterer Folge auch alleine verwenden können wie zB. für Rechnungen oder Homepage .
Angaben auf der Etikette wie oben beschrieben:
Imkerei
T & L Wimmerhuber
Tannenhoferweg 214
9563 Tannberg
+436608274316 1,2 mm ausgehend vom kleinsten Buchstaben
Mindestens Haltbar bis:
siehe Glasunterseite
Trocken und vor Wärme geschützt Lagern ! 1,2 mm ausgehend vom kleinsten Buchstaben

```html
<!DOCTYPE html>
<html lang="de">
<head>
<meta charset="utf-8">
<title>Kolmer`s Honig – Etikett Wald-Blüten 500 g</title>
<link href="https://fonts.googleapis.com/css2?family=Poppins:wght@400;500;600&display=swap" rel="stylesheet">
<style>
  :root {
    --stage: #2b2b2b;
    --label-dark: #262626;
    --label-mid: #303030;
    --honey-yellow: #f2c230;
    --ink-white: #ffffff;
    --divider: #e0a92a;
  }
  * { margin: 0; padding: 0; box-sizing: border-box; }
  html, body { width: 1200px; height: 1200px; overflow: hidden; }
  body {
    background: var(--stage);
    font-family: "Poppins", sans-serif;
    color: var(--ink-white);
    position: relative;
  }
  .label {
    position: absolute;
    left: 0; top: 423px;
    width: 1200px; height: 354px;
  }
  .label__texture {
    position: absolute; inset: 18px 0;
    background: radial-gradient(ellipse at 60% 50%, var(--label-mid) 0%, var(--label-dark) 75%);
  }
  .label__stripe {
    position: absolute; left: 0; width: 100%; height: 18px;
    background: var(--honey-yellow);
  }
  .label__stripe--top { top: 0; }
  .label__stripe--bottom { bottom: 0; }
  .info {
    position: absolute; left: 24px; width: 216px;
    text-align: center; font-size: 14px; line-height: 18px; font-weight: 400;
  }
  .info--address { top: 40px; }
  .info__divider {
    position: absolute; left: 24px; top: 152px; width: 216px; height: 1px;
    background: var(--divider);
  }
  .info--details { top: 174px; }
  .info__weight { font-size: 25px; line-height: 34px; margin: 3px 0 4px; }
  .brand {
    position: absolute; left: 380px; top: 114px;
    display: flex; align-items: center; gap: 18px;
  }
  .brand__dot {
    width: 34px; height: 34px; border-radius: 50%;
    background: var(--honey-yellow);
  }
  .brand__name {
    font-size: 70px; font-weight: 500; line-height: 1; letter-spacing: 0.5px;
    color: var(--ink-white);
  }
  .variety {
    position: absolute; left: 790px; top: 212px;
    font-size: 21px; font-weight: 600; color: var(--ink-white);
  }
</style>
</head>
<body>
  <section class="label">
    <div class="label__stripe label__stripe--top" role="img" aria-label="Gelbes Zickzack-Band"></div>
    <div class="label__texture" role="img" aria-label="Dunkelgrauer Hintergrund mit feinem Wabenmuster"></div>
    <div class="label__stripe label__stripe--bottom" role="img" aria-label="Gelbes Zickzack-Band"></div>

    <div class="info info--address">
      Imkerei<br>
      T &amp; L Wimmerhuber<br>
      Tannenhoferweg 214<br>
      9563 Tannberg<br>
      +436608274316
    </div>
    <div class="info__divider"></div>
    <div class="info info--details">
      100% Honig aus Österreich
      <div class="info__weight">500g</div>
      Mindestens Haltbar bis:<br>
      siehe Glasunterseite<br>
      Trocken und vor Wärme<br>
      geschützt Lagern !
    </div>

    <div class="brand">
      <span class="brand__dot"></span>
      <span class="brand__name">Kolmer`s Honig</span>
    </div>
    <div class="variety">Wald-Blüten</div>
  </section>
</body>
</html>
```